TGV Electricial Contracting Services

Hi guys, after a design for my small electrical company, have logo design files to be incorporated into the layout, the basic concept is electrical contracting services for residential, commercial, industrial & data services, image is clean clear and strong,

Card format is to have a nice clean logo on front,with maybe the Residential – commercial – industrial - data, followed with licensed & insured, followed by contact details on backside of the card.

Target Market(s)

Residential, commercial, industrial sectors.

Industry/Entity Type

Electrical

Contact Information for Business Card

TGV logo,
Residential – commercial – industrial - data
REC: 57310
Email: tgv@wavolink.net.au
Phone: 0472 358 129

Requirements
Must have
• Clean & strong design.
Nice to have
• If possible, I would like the logo colours inverted so the text is orange and the background is black on the front of the card, then the backside of the card be the reverse colour
Should not have
• No Sparks, lightning bolts,

```html
<!DOCTYPE html>
<html lang="en">
<head>
<meta charset="utf-8">
<title>TGV Electrical – Business Card</title>
<link rel="stylesheet" href="https://fonts.googleapis.com/css2?family=Exo+2:ital,wght@0,400;0,600;0,700;1,400&display=swap">
<style>
  :root {
    --orange: #f47b20;
    --black: #0b0b0b;
    --white: #ffffff;
    --backdrop: #e8e8e6;
    --card-w: 517px;
    --card-h: 296px;
  }
  * { margin: 0; padding: 0; box-sizing: border-box; }
  html, body {
    width: 1200px; height: 521px; overflow: hidden;
    background: var(--backdrop);
    font-family: "Exo 2", sans-serif;
  }
  .canvas { position: relative; width: 1200px; height: 521px; }
  .card {
    position: absolute; top: 112px;
    width: var(--card-w); height: var(--card-h);
    overflow: hidden;
  }
  .card--front { left: 60px; background: var(--black); }
  .card--back { left: 623px; background: var(--orange); }

  .wordmark {
    position: absolute; font-weight: 600; line-height: 1; letter-spacing: 1px;
    white-space: nowrap;
  }
  .company-name {
    position: absolute; font-weight: 600; line-height: 1; white-space: nowrap;
  }

  /* front */
  .card--front .wordmark { left: 0; right: 0; top: 82px; text-align: center; color: var(--orange); font-size: 72px; }
  .card--front .company-name { left: 0; right: 0; top: 158px; text-align: center; color: var(--orange); font-size: 19px; }
  .tagline {
    position: absolute; left: 0; right: 0; top: 201px;
    text-align: center; color: var(--white);
    font-style: italic; font-size: 16.5px; line-height: 21px;
  }

  /* back */
  .back-corner { position: absolute; inset: 0; width: 100%; height: 100%; }
  .card--back .wordmark { left: 34px; top: 24px; color: var(--white); font-size: 60px; }
  .card--back .company-name { left: 34px; top: 94px; color: var(--white); font-size: 15px; }
  .services {
    position: absolute; left: 276px; top: 20px; list-style: none;
    color: var(--white); font-size: 16px; line-height: 18.5px;
  }
  .contact { position: absolute; left: 40px; top: 188px; list-style: none; color: var(--white); font-size: 22px; }
  .contact li { display: flex; align-items: center; gap: 8px; height: 29px; }
  .contact svg { width: 20px; height: 20px; flex: none; }
  .mini-mark {
    position: absolute; right: 18px; bottom: 22px; text-align: center; color: var(--white);
  }
  .mini-mark__name { display: block; font-weight: 600; font-size: 26px; line-height: 1; letter-spacing: 1px; }
  .mini-mark__sub { display: block; font-weight: 600; font-size: 6px; margin-top: 2px; }
</style>
</head>
<body>
<main class="canvas">
  <section class="card card--front" aria-label="Card front">
    <p class="wordmark">TGV</p>
    <p class="company-name">Tom Grant Vale Electrical</p>
    <p class="tagline">Electrical contracting services for residential,<br>commercial, industrial &amp; data services.</p>
  </section>

  <section class="card card--back" aria-label="Card back">
    <svg class="back-corner" viewBox="0 0 517 296" preserveAspectRatio="none" aria-hidden="true">
      <polygon points="517,0 517,296 284,296" fill="var(--black)"/>
    </svg>
    <p class="wordmark">TGV</p>
    <p class="company-name">Tom Grant Vale Electrical</p>
    <ul class="services">
      <li>Residential</li>
      <li>Commercial</li>
      <li>Industrial</li>
      <li>Data</li>
      <li>REC: 57310</li>
    </ul>
    <ul class="contact">
      <li>
        <svg viewBox="0 0 20 20" aria-hidden="true">
          <rect x="1" y="3" width="18" height="5" rx="2" fill="var(--black)"/>
          <rect x="3" y="8" width="14" height="11" rx="1.5" fill="var(--black)"/>
          <g fill="var(--orange)">
            <rect x="5.5" y="10.5" width="2" height="2"/><rect x="9" y="10.5" width="2" height="2"/><rect x="12.5" y="10.5" width="2" height="2"/>
            <rect x="5.5" y="14" width="2" height="2"/><rect x="9" y="14" width="2" height="2"/><rect x="12.5" y="14" width="2" height="2"/>
          </g>
        </svg>
        <span>0472.358.129</span>
      </li>
      <li>
        <svg viewBox="0 0 20 20" aria-hidden="true">
          <rect x="1" y="5" width="18" height="12" fill="var(--black)"/>
          <polyline points="1,5 10,12 19,5" fill="none" stroke="var(--orange)" stroke-width="1.5"/>
        </svg>
        <span>tgv@wavolink.net.au</span>
      </li>
    </ul>
    <div class="mini-mark">
      <span class="mini-mark__name">TGV</span>
      <span class="mini-mark__sub">Tom Grant Vale Electrical</span>
    </div>
  </section>
</main>
</body>
</html>
```